◆遺体の目的/概要
電子書籍(novrel)の表紙のデザインをお願いします。

◆画像のサイズ
表紙ファイルの理想的な寸法は2,560✕1,600ピクセルです。
注:画像の寸法は1,000✕625ピクセル以上であることが必要です。
画像の最大の寸法は10,000✕10,000ピクセルです。

◆タイトル
外国人と一緒に働くすべての人へ
「ソラーレ・ポルト・メトリクス」
Solare Porto Metrics
少子高齢化の社会を生き残る強い会社を作る方法

◆著者
外国人ブリッジコーディネーター
橋本 健吾

◆本の内容
少子高齢化が進む社会にあって、
外国人労働者の必要性や、彼らが働きやす職場環境作りの必要性
どんなコミュニケーションが必要かという事を解説した本です。
※本文を参考資料として添付します。

◆デザイン要望
会社や企業向けなので、プロフェッショナルなイメージ
グローバルなイメージ(目を引く外国人の写真など)
でよろしくお願い致します。

※次点、次々点の方への参加報酬も設定いたします。

※その他、必要な情報がありましたらお問い合せください。

本文の内容に該当する登場人物のイメージを用いている点や
「強い会社を作る」という主なテーマが強調されていいる点など、
ぱっと見て分かりやすいものを選ばせていただきました。

ほんとにどれもセンスを感じられるものだったので、
選定するのに、とても時間がかかりました。
同じテーマで、こんなにも色々なアイデアがあること
その多様性に感動しました。
皆さんが時間をかけて、考えてくださったことに感謝致します。
今後も出版を考えていますので、また依頼の際は多くの方の提案をよろしくお願い致します!

```html
<!DOCTYPE html>
<html lang="ja">
<head>
<meta charset="utf-8">
<title>ソラーレ・ポルト・メトリクス</title>
<link rel="stylesheet" href="https://fonts.googleapis.com/css2?family=Noto+Sans+JP:wght@500;700;900&family=Montserrat:wght@800&display=swap">
<style>
  :root {
    --blue: #1d87c6;
    --orange: #f4991c;
    --navy: #1d2b45;
    --ink: #222222;
    --paper: #ffffff;
  }
  html, body { margin: 0; padding: 0; overflow: hidden; background: var(--paper); }
  .cover {
    position: relative;
    width: 750px;
    height: 1200px;
    overflow: hidden;
    background: var(--paper);
    font-family: "Noto Sans JP", sans-serif;
  }
  .cover-photo {
    position: absolute;
    left: 0; top: 487px;
    width: 750px; height: 375px;
    background: linear-gradient(135deg, #8a9aa8 0%, #c9cfd4 35%, #5b6470 60%, #d9d2c8 100%);
  }
  .latin-title {
    position: absolute;
    left: 62px; top: 20px;
    transform-origin: left top;
    transform: rotate(90deg);
    font-family: "Montserrat", sans-serif;
    font-weight: 800;
    font-size: 62px;
    letter-spacing: 1px;
    color: var(--orange);
    white-space: nowrap;
    line-height: 1;
  }
  .tagline-box {
    position: absolute;
    right: 0; top: 0;
    width: 190px; height: 285px;
    background: var(--blue);
    display: flex;
    flex-direction: row-reverse;
    justify-content: center;
    gap: 10px;
    padding-top: 14px;
    box-sizing: border-box;
  }
  .tagline-box span {
    writing-mode: vertical-rl;
    color: var(--paper);
    font-weight: 900;
    font-size: 29px;
    line-height: 1.2;
  }
  .main-title span {
    position: absolute;
    top: 30px;
    writing-mode: vertical-rl;
    font-weight: 900;
    font-size: 90px;
    line-height: 1;
    color: var(--blue);
    text-shadow: 0 0 4px #fff, 0 0 4px #fff, 0 0 6px #fff;
  }
  .main-title .col-1 { left: 455px; }
  .main-title .col-2 { left: 288px; }
  .main-title .col-3 { left: 160px; }
  .theme-box {
    position: absolute;
    left: 287px; top: 862px;
    width: 438px; height: 188px;
    background: var(--orange);
    display: flex;
    flex-direction: column;
    justify-content: center;
    align-items: center;
    gap: 4px;
  }
  .theme-box span {
    font-weight: 900;
    font-size: 40px;
    line-height: 1.2;
    color: var(--paper);
  }
  .theme-box .emphasis { color: var(--navy); font-size: 38px; }
  .author {
    position: absolute;
    right: 30px; top: 1068px;
    text-align: right;
    color: var(--ink);
  }
  .author-role { font-weight: 700; font-size: 22px; margin: 0; }
  .author-name { font-weight: 900; font-size: 48px; margin: 4px 0 0; letter-spacing: 2px; }
  .author-name small { font-size: 28px; margin-left: 8px; }
</style>
</head>
<body>
  <div class="cover">
    <div class="cover-photo" role="img" aria-label="ビジネスパーソンたちが会議室のテーブルを囲んで話し合う写真"></div>

    <div class="latin-title">Solare Porto Metrics</div>

    <div class="tagline-box">
      <span>外国人と一緒に働く</span>
      <span>すべての人へ</span>
    </div>

    <h1 class="main-title">
      <span class="col-1">ソラーレ・</span>
      <span class="col-2">ポルト・</span>
      <span class="col-3">メトリクス</span>
    </h1>

    <div class="theme-box">
      <span>少子高齢化の</span>
      <span>社会を生き残る</span>
      <span class="emphasis">強い会社を作る方法</span>
    </div>

    <div class="author">
      <p class="author-role">外国人ブリッジコーディネーター</p>
      <p class="author-name">橋本 健吾<small>著</small></p>
    </div>
  </div>
</body>
</html>
```